Fasteners Poly-bag design with VANTRO brand

We are trading with fasteners and rigging hardware and now we need a new design for a poly-bag. The header of poly-bag will contain two parts - top part (around 60%) will be static with our logo "VANTRO" and your type of design. The bottom part (around 40%) should be with different color for each group of fasteners or rigging hardware and with different text (5 groups in total). The border between the two part can be different from straight line (for example like wave or something else). I added a file with explanation and some samples of poly-bags. The total dimensions of the header are 80 mm/40 mm. The nylon part of poly-bag will have a background - I added a file with our image, but you can offer us different image also. Please when creating design, do it for full poly-bag, including the nylon part, not only header. The colors from header can continue to the nylon part also. I added a file "DESIGN SAMPLES" just as examples, what we expect to see. Of course you can offer your own variant of design! Thank you in advance!

Target Market(s)

Fasteners and rigging hardware

Industry/Entity Type

Fastener

Font styles to use
Other font styles liked:
• SAUCER BB - Logo Font

Colors

Designer to choose colors to be used in the design.

Requirements
Must have
• Our logo "VANTRO"

```html
<!DOCTYPE html>
<html lang="en">
<head>
<meta charset="utf-8">
<title>VANTRO Fasteners – Wood Screws Poly-bag Header</title>
<link rel="stylesheet" href="https://fonts.googleapis.com/css2?family=Krona+One&family=Arimo:wght@400;700&display=swap">
<style>
  :root {
    --royal-blue: #1a47a0;
    --navy-blue: #102a6b;
    --title-shadow: #0b1f55;
    --silver-light: #ffffff;
    --silver-mid: #d9dadc;
    --silver-dark: #a9abae;
    --graphite: #6d6e70;
    --ink: #111111;
    --white: #ffffff;
  }
  html, body {
    margin: 0;
    padding: 0;
    width: 800px;
    height: 1200px;
    overflow: hidden;
    background: var(--white);
  }
  .polybag {
    position: relative;
    width: 800px;
    height: 1200px;
    overflow: hidden;
  }
  .polybag-art {
    position: absolute;
    inset: 0;
    display: block;
  }
  .brand-logo {
    position: absolute;
    left: 44px;
    top: 196px;
    font-family: "Krona One", sans-serif;
    font-size: 62px;
    line-height: 1;
    color: var(--ink);
    letter-spacing: 0;
    transform: rotate(-8deg);
    transform-origin: left center;
  }
  .tagline,
  .product-title { font-family: "Krona One", sans-serif; }
  .size-label,
  .pack-count { font-family: "Arimo", sans-serif; }
</style>
</head>
<body>
<main class="polybag">
  <svg class="polybag-art" viewBox="0 0 800 1200" width="800" height="1200" xmlns="http://www.w3.org/2000/svg">
    <defs>
      <linearGradient id="silverSheen" x1="0" y1="0" x2="1" y2="0.4">
        <stop offset="0" stop-color="var(--silver-light)"/>
        <stop offset="0.55" stop-color="#f4f4f5"/>
        <stop offset="1" stop-color="var(--silver-mid)"/>
      </linearGradient>
      <linearGradient id="blueBand" x1="0" y1="0" x2="1" y2="0">
        <stop offset="0" stop-color="var(--navy-blue)"/>
        <stop offset="0.35" stop-color="var(--royal-blue)"/>
        <stop offset="0.75" stop-color="var(--navy-blue)"/>
        <stop offset="1" stop-color="var(--royal-blue)"/>
      </linearGradient>
      <linearGradient id="silverStripe" x1="0" y1="0" x2="1" y2="0">
        <stop offset="0" stop-color="var(--silver-mid)"/>
        <stop offset="0.5" stop-color="var(--silver-light)"/>
        <stop offset="1" stop-color="var(--silver-dark)"/>
      </linearGradient>
      <linearGradient id="screwArea" x1="0" y1="0" x2="1" y2="0">
        <stop offset="0" stop-color="#ececed"/>
        <stop offset="1" stop-color="#f8f8f8"/>
      </linearGradient>
    </defs>

    <!-- header background -->
    <rect class="header-bg" x="0" y="0" width="800" height="620" fill="url(#silverSheen)"/>

    <!-- top corner band -->
    <polygon class="corner-band" points="0,0 464,0 0,107" fill="url(#blueBand)"/>
    <polygon class="corner-band-edge" points="464,0 520,0 0,145 0,107" fill="url(#silverStripe)"/>

    <!-- hang hole -->
    <path class="hang-hole" d="M312 64 H362 A42 42 0 0 1 438 64 H488 A19 19 0 0 1 507 84 A19 19 0 0 1 488 104 H312 A19 19 0 0 1 293 84 A19 19 0 0 1 312 64 Z" fill="var(--white)" stroke="var(--ink)" stroke-width="1.2"/>

    <!-- main diagonal band with silver edges -->
    <polygon class="band-edge-top" points="0,380 800,140 800,197 0,437" fill="url(#silverStripe)" opacity="0.7"/>
    <polygon class="product-band" points="0,437 800,197 800,368 0,608" fill="url(#blueBand)"/>
    <polygon class="band-edge-bottom" points="0,608 800,368 800,378 0,620" fill="url(#silverStripe)"/>

    <!-- size tab -->
    <polygon class="size-tab" points="533,368 800,288 800,339 584,408" fill="url(#silverStripe)"/>

    <!-- lower white body -->
    <polygon class="bag-body" points="0,620 800,378 800,1200 0,1200" fill="var(--white)"/>

    <!-- screw assortment illustration area -->
    <polygon class="screw-illustration" role="img" aria-label="Line illustration of assorted wood screws, eye screw and nail" points="0,606 96,584 232,1200 0,1200" fill="url(#screwArea)"/>

    <!-- bottom band -->
    <polygon class="footer-edge" points="315,1200 800,1045 800,1077 405,1200" fill="url(#silverStripe)"/>
    <polygon class="footer-band" points="405,1200 800,1077 800,1200" fill="url(#blueBand)"/>

    <!-- text -->
    <text class="tagline" x="459" y="188" transform="rotate(-21 459 188)" font-size="31" fill="var(--graphite)" textLength="245" lengthAdjust="spacingAndGlyphs">FASTENERS</text>
    <g class="product-title-group" transform="rotate(-20 259 427)">
      <text class="product-title" x="262" y="430" font-size="64" fill="var(--title-shadow)" textLength="533" lengthAdjust="spacingAndGlyphs">WOOD SCREWS</text>
      <text class="product-title" x="259" y="427" font-size="64" fill="var(--white)" textLength="533" lengthAdjust="spacingAndGlyphs">WOOD SCREWS</text>
    </g>
    <text class="size-label" x="592" y="387" transform="rotate(-21 592 387)" font-size="40" fill="var(--ink)" textLength="178" lengthAdjust="spacingAndGlyphs"><tspan font-size="28">Size : </tspan>2 Inch</text>
    <text class="pack-count" x="643" y="1167" font-weight="700" fill="var(--white)"><tspan font-size="37">100</tspan><tspan font-size="26" dx="6">Nos.</tspan></text>
  </svg>

  <div class="brand-logo">VANTRO</div>
</main>
</body>
</html>
```